Business card for our large format printing and installation business

We want a professional looking business card for our business. We manufacture and install Signs.

On the back of the card add this info
Large Format Graphics Printing & Installations, Event Graphics, Banners, Posters, Vehicle Fleet Graphics, Boat Wraps, Wall Murals, Decals,Displays,Signs,Plaques,Digital Signs

On the Front of the card add the Tallowfern Signs logo, plus On the back of the card add the Orange Tallowfern Wraps logo. The 2 vector logos are attached to the design brief.

Target Market(s)

Local business owners

Contact Information for Business Card

Colors
f37122
f68d4e
f9ba93

Requirements
Must have
• On the Front of the card add the Tallowfern Signs logo, plus On the back of the card add the Orange Tallowfern Wraps logo. The 2 vector logos are attached to the design brief.

```html
<!DOCTYPE html>
<html lang="en">
<head>
<meta charset="utf-8">
<title>Tallowfern Signs Business Card</title>
<link href="https://fonts.googleapis.com/css2?family=Manrope:wght@400;500;700;800&display=swap" rel="stylesheet">
<style>
  :root {
    --bg: #e9e9eb;
    --card-dark: #141414;
    --card-light: #ffffff;
    --orange: #f37122;
    --orange-mid: #f68d4e;
    --orange-light: #f9ba93;
    --ink: #2a2a2a;
    --ink-soft: #555;
  }
  * { margin: 0; padding: 0; box-sizing: border-box; }
  html, body {
    width: 1200px; height: 794px; overflow: hidden;
    background: var(--bg);
    font-family: "Manrope", sans-serif;
  }
  .stage { position: relative; width: 1200px; height: 794px; }

  .card {
    position: absolute; width: 525px; height: 300px;
    border-radius: 3px; overflow: hidden;
    box-shadow: 0 6px 18px rgba(0,0,0,.12);
  }

  /* Front (dark) */
  .card-front { left: 70px; top: 120px; background: var(--card-dark); }
  .card-front .brand-name {
    position: absolute; left: 0; right: 0; top: 96px; text-align center;
    text-align: center;
    font-weight: 800; font-size: 50px; letter-spacing: -0.5px;
    color: var(--orange); line-height: 1;
  }
  .card-front .rule {
    position: absolute; left: 150px; right: 0; top: 168px;
    height: 3px; background: var(--orange-mid);
  }
  .card-front .website {
    position: absolute; left: 0; right: 0; top: 208px; text-align: center;
    font-size: 15px; font-weight: 500; letter-spacing: 1px; color: var(--orange-mid);
  }
  .card-front .band {
    position: absolute; left: 0; right: 0; bottom: 22px;
    height: 5px; background: var(--orange);
  }

  /* Back (light) */
  .card-back { left: 605px; top: 374px; background: var(--card-light); }
  .services {
    position: absolute; left: 24px; right: 24px; top: 14px;
    font-size: 10px; font-weight: 500; line-height: 1.45;
    color: var(--ink-soft); text-align: center;
  }
  .services strong { color: var(--orange); font-weight: 700; }
  .card-back .brand-name {
    position: absolute; left: 34px; top: 132px; width: 210px;
    font-weight: 800; font-size: 31px; line-height: 1;
    color: var(--orange); letter-spacing: -0.3px;
  }
  .contact { position: absolute; left: 262px; top: 72px; }
  .person {
    border-left: 3px solid var(--orange); padding-left: 14px; margin-bottom: 18px;
  }
  .person-name { font-size: 17px; font-weight: 700; color: var(--ink); letter-spacing: .5px; }
  .person-role { font-size: 13px; color: var(--ink-soft); margin-top: 3px; }
  .contact-list { list-style: none; }
  .contact-list li {
    display: flex; align-items: flex-start; gap: 10px;
    font-size: 13px; color: var(--ink); line-height: 1.35; margin-bottom: 5px;
  }
  .contact-list svg { flex: none; width: 14px; height: 14px; margin-top: 2px; }
  .card-back .band-accent {
    position: absolute; left: 0; right: 0; bottom: 14px; height: 8px;
    background: linear-gradient(90deg, var(--orange), var(--orange-light) 55%, var(--orange));
  }
  .card-back .band-base {
    position: absolute; left: 0; right: 0; bottom: 0; height: 14px; background: var(--card-dark);
  }
</style>
</head>
<body>
<main class="stage">
  <section class="card card-front">
    <div class="brand-name">Tallowfern Signs</div>
    <div class="rule"></div>
    <div class="website">www.tallowfernwraps.com</div>
    <div class="band"></div>
  </section>

  <section class="card card-back">
    <p class="services"><strong>Large Format Graphics Printing &amp; Installations</strong> · Event Graphics · Banners · Posters<br>Vehicle Fleet Graphics · Boat Wraps · Wall Murals · Decals · Displays · Signs · Plaques · Digital Signs</p>
    <div class="brand-name">Tallowfern Signs</div>
    <div class="contact">
      <div class="person">
        <div class="person-name">DANA WHITLOCK</div>
        <div class="person-role">CEO</div>
      </div>
      <ul class="contact-list">
        <li>
          <svg viewBox="0 0 24 24" fill="none" stroke="#f37122" stroke-width="2"><path d="M5 3h4l2 5-3 2a12 12 0 0 0 6 6l2-3 5 2v4a2 2 0 0 1-2 2A17 17 0 0 1 3 5a2 2 0 0 1 2-2z"/></svg>
          555-014-2270
        </li>
        <li>
          <svg viewBox="0 0 24 24" fill="none" stroke="#f37122" stroke-width="2"><rect x="7" y="2" width="10" height="20" rx="2"/><line x1="11" y1="18" x2="13" y2="18"/></svg>
          555-018-3391
        </li>
        <li>
          <svg viewBox="0 0 24 24" fill="none" stroke="#f37122" stroke-width="2"><rect x="3" y="5" width="18" height="14" rx="1"/><path d="M3 6l9 7 9-7"/></svg>
          dana@tallowfern.net
        </li>
        <li>
          <svg viewBox="0 0 24 24" fill="none" stroke="#f37122" stroke-width="2"><path d="M12 22s7-7 7-12a7 7 0 0 0-14 0c0 5 7 12 7 12z"/><circle cx="12" cy="10" r="2.5"/></svg>
          <span>1480 Harbor Mill Lane #4<br>Cedar Point, FL 30000</span>
        </li>
      </ul>
    </div>
    <div class="band-accent"></div>
    <div class="band-base"></div>
  </section>
</main>
</body>
</html>
```